Pelmora needs stationery design

We need desings for presentation cards and letter head for our company. It would be better that the letterhead uses our logo with white background and the presentation card the logo with the black background for the back of the card and the text (name, phone
Updates

Necesitas un par de días antes de escoger al ganador

Colors
0455a3
ec1f27
000000

Requirements
Must have
• Use company logo and colors

```html
<!DOCTYPE html>
<html lang="en">
<head>
<meta charset="utf-8">
<title>Pelmora Letterhead</title>
<link href="https://fonts.googleapis.com/css2?family=Questrial&family=Roboto:wght@400;700&display=swap" rel="stylesheet">
<style>
  :root {
    --brand-blue: #0455a3;
    --brand-red: #ec1f27;
    --brand-black: #000000;
    --backdrop: #e6e6e6;
    --paper-top: #f4f4f4;
    --paper-bottom: #e2e2e2;
    --text-body: #4a4a4a;
    --text-contact: #3c3c3c;
    --rule: #8a8a8a;
  }
  * { margin: 0; padding: 0; box-sizing: border-box; }
  html, body {
    width: 1024px; height: 1200px; overflow: hidden;
    background: var(--backdrop);
  }
  .letterhead {
    position: absolute; left: 98px; top: 20px;
    width: 827px; height: 1160px;
    background: linear-gradient(160deg, var(--paper-top) 0%, #ececec 55%, var(--paper-bottom) 100%);
    box-shadow: 0 2px 6px rgba(0,0,0,0.12);
    font-family: "Questrial", "Century Gothic", sans-serif;
    color: var(--text-body);
  }
  .accent-bar { position: absolute; top: 74px; width: 11px; height: 122px; }
  .accent-bar--left { left: 0; background: var(--brand-red); }
  .accent-bar--right { right: 0; background: var(--brand-blue); }
  .brand-name {
    position: absolute; left: 77px; top: 110px;
    font-family: "Roboto", sans-serif; font-weight: 700;
    font-size: 38px; letter-spacing: 1px; line-height: 1;
    color: var(--brand-black); text-transform: uppercase;
  }
  .contact-block {
    position: absolute; left: 595px; top: 77px; height: 111px;
    border-left: 1px solid var(--rule);
    padding-left: 18px;
    font-family: "Roboto", sans-serif; font-size: 12.5px;
    color: var(--text-contact); line-height: 16px;
  }
  .contact-block .address { margin-top: 1px; }
  .contact-line { display: flex; align-items: center; gap: 6px; }
  .contact-line svg { width: 11px; height: 11px; fill: var(--brand-blue); flex: none; }
  .salutation {
    position: absolute; left: 77px; top: 302px;
    font-size: 21px; color: #555;
  }
  .letter-body {
    position: absolute; left: 77px; top: 362px; width: 680px;
    font-size: 11.8px; line-height: 15.3px; text-align: justify;
  }
  .letter-body p { margin-bottom: 15.3px; }
  .closing {
    position: absolute; left: 77px; top: 733px; font-size: 11.8px;
  }
  .signature {
    position: absolute; left: 77px; top: 800px; width: 142px; height: 66px;
    background: linear-gradient(90deg, rgba(4,85,163,0.18), rgba(4,85,163,0.08));
    border-radius: 4px;
  }
</style>
</head>
<body>
  <main class="letterhead">
    <div class="accent-bar accent-bar--left"></div>
    <div class="accent-bar accent-bar--right"></div>

    <div class="brand-name">Pelmora</div>

    <address class="contact-block" style="font-style:normal">
      <div class="address">1240 Alder Crest Road<br>Fairbrook, Alaska 99812</div>
      <div class="contact-line">
        <svg viewBox="0 0 16 16"><path d="M3.6 1.2l2.3 2.9-1.3 1.8c.9 2 2.5 3.6 4.5 4.5l1.8-1.3 2.9 2.3-1.4 2.4C7 13.4 2.6 9 1.2 2.6z"/></svg>
        <span>555 210 4871</span>
      </div>
      <div class="contact-line">
        <svg viewBox="0 0 16 16"><path d="M4.5 0h7a1 1 0 011 1v14a1 1 0 01-1 1h-7a1 1 0 01-1-1V1a1 1 0 011-1zm.5 2v10h6V2zm3 11a1 1 0 100 2 1 1 0 000-2z"/></svg>
        <span>555 736 0192</span>
      </div>
      <div class="contact-line">
        <svg viewBox="0 0 16 16"><path d="M4 1h8v4H4zM1 6h14v7h-3v2H4v-2H1zm4 5v3h6v-3zm8-3a1 1 0 100 2 1 1 0 000-2z"/></svg>
        <span>555 384 6627</span>
      </div>
      <div class="contact-line">
        <svg viewBox="0 0 16 16"><path d="M0 3h16v1.2L8 9 0 4.2zm0 2.6l8 4.8 8-4.8V13H0z"/></svg>
        <span>info@pelmora.com</span>
      </div>
      <div class="contact-line">
        <svg viewBox="0 0 16 16"><path d="M8 0a8 8 0 110 16A8 8 0 018 0zm-1 3.5L4 5l1 2 2 .5.5 2L6 12l1.5 2 1-3 2-1.5-1-2H7.5l-.5-1.5 1.5-1L9 2z"/></svg>
        <span>www.pelmora.com</span>
      </div>
    </address>

    <p class="salutation">Dear Mr. Hale,</p>

    <section class="letter-body">
      <p>Lorem ipsum dolor sit amet, consectetur adipiscing elit. Donec orci purus, luctus vitae dignissim eu, iaculis sed purus. Vivamus faucibus, ipsum nec aliquet viverra, leo mauris condimentum ligula, sit amet sagittis enim ligula quis arcu. Nam egestas tortor id nisi porttitor mattis. In tortor ante, ultricies in suscipit a, tempus non massa. Vivamus et auctor mi. Fusce vel massa nulla. Phasellus nec eros mauris, et scelerisque orci.</p>
      <p>Donec malesuada orci vitae nulla accumsan porta a id massa. Quisque accumsan iaculis magna sit amet fringilla. Maecenas consequat, magna eget tincidunt semper, odio nibh rutrum mi, id feugiat ante nisi eu risus. Vestibulum nunc orci, rhoncus a placerat in, ultricies in mi. Cras mattis varius eros, vel fringilla nisi suscipit eget. Quisque scelerisque sagittis nulla at porttitor.</p>
      <p>Sed id augue vitae urna euismod commodo aliquet a quam. Pellentesque arcu velit, cursus et malesuada ut, consequat et diam. Nullam erat sem, rhoncus id ullamcorper vitae, rhoncus et arcu. In ultricies ultricies nulla, ut rutrum nisi iaculis at. Donec eu magna a metus ornare faucibus. Fusce aliquet faucibus ultricies. Morbi semper, est id tincidunt gravida, sem arcu adipiscing lacus, ac bibendum nulla leo eu purus. Quisque nec diam sed risus consectetur a ccumsan quis quis nibh. Vestibulum id purus lorem.</p>
      <p>It is a long established fact that a reader will be distracted by the readable content of a page when looking at its layout. The point of using Lorem Ipsum is that it has a more-or-less normal distribution of letters, as opposed to using 'Content here, content here', making it look like readable English. Many desktop publishing packages</p>
    </section>

    <p class="closing">Sincerely,</p>

    <div class="signature" role="img" aria-label="Handwritten signature of Dorian Hale in blue ink"></div>
  </main>
</body>
</html>
```